Brightwell Capital - fund management and algorithmic design

We're looking for a web design for a new company called brightwell capital which is based out of London.

The photography provided will be a major part of the creative content. The intent is to have a sharp, clear, professional, slick look. Less is more and clutter is not the root that should be followed.

A logo has been selected and the photography provided will give the designer a good idea of what we are looking for. The logo designer is still getting back to me with the very final version but what is provided is good enough to move forward with. the final design will likely have this changed slightly.

The photos are about 1.2 meg each at 86 pdi. I believe this is about right for a high quality web image.

At some point on the site it should have: Integrity, Innovative, Progressive. These are core principles of the company. Also ,Fund management and algorithmic design could be used somewhere as this explains exactly what we do.

I also wish to have the secondary pages designed too. However, rather than asking everybody to do this i will ask a select few designers to look at one of the pages. The chosen designer will then be asked to finish the other pages too. These are expected to be quite simple, nothing fussy - clean and presentable with a small amount of room for artistic license.

Also the links to these two sites will give you a very good idea of what we're looking for.

quendor.com
tavelpointrix.com
birchwardlanefx.com
Updates

Hi,

sorry for as i had problem getting the final images from the photographer as he's been away and busy.

However, we now the the logo (be it not the very final version) and the photos uploaded.  Please read the brief again as this has been updated too.

Initially i'd be happy if you made up the front page and after that i will ask a small handful of designers to submit a design for the secondary page - this way i feel is better as it uses less of your time.  These pages are likely to use the photography for a backdrop too.

Looking forward to your designs.

Regards,

Dominic

Reason: I have extended the deadline as the first week has been held up because of delays in content. thanks, Dominic

Target Market(s)

wealth individuals who wish to diversify their investment portfolios with investments predominantly in the foreign exchange markets as well as some financial products offered by ZPLHoldings.com

Industry/Entity Type

It Company

Requirements
Must have
• There are three photos that the site must use, once the final design is fully operational and coded we want the first three photos to rotate on the front page. Much like quendorr.com

An area where a prospective client can enter their email address to receive market new letters and correspondences from brightwell capital.

front page

about us,
managed accounts
systems and performance

```html
<!DOCTYPE html>
<html lang="en">
<head>
<meta charset="utf-8">
<title>Brightwell Capital</title>
<link href="https://fonts.googleapis.com/css2?family=Carlito:wght@400;700&family=Sintony:wght@400;700&family=Open+Sans:wght@400;600&display=swap" rel="stylesheet">
<style>
:root{
  --blue:#2e6fb0;
  --blue-bright:#1f8fe0;
  --link:#2566a8;
  --ink:#3b3b3b;
  --muted:#9a9a9a;
  --band:#f3f3f3;
  --dark:#474747;
  --dark-text:#c8c8c8;
  --footer:#f1f1f1;
  --white:#ffffff;
}
*{margin:0;padding:0;box-sizing:border-box}
html,body{width:1093px;height:1200px;overflow:hidden}
body{position:relative;background:var(--white);font-family:"Open Sans",sans-serif;color:var(--ink)}
.hero-photo{position:absolute;left:0;top:0;width:1093px;height:754px;
  background:linear-gradient(180deg,#6f6a68 0%,#8a8583 9%,#77726f 20%,#4b4848 30%,#3a3838 50%,#2c2b2b 75%,#3a3a3a 100%)}
.topbar{position:absolute;left:0;top:0;width:1093px;height:36px}
.call{position:absolute;left:722px;top:12px;font-family:"Sintony",sans-serif;font-size:11.5px;font-weight:700;color:var(--white)}
.social{position:absolute;top:8px;width:20px;height:20px;border-radius:3px}
.nav-band{position:absolute;left:0;top:36px;width:1093px;height:44px;
  background:linear-gradient(180deg,#ffffff 0%,#f4f4f4 55%,#e2e2e2 100%);border-bottom:1px solid #cfcfcf}
.nav a{position:absolute;top:15px;font-family:"Sintony",sans-serif;font-size:12.5px;color:#333;text-decoration:none}
.brand{position:absolute;left:120px;top:15px;width:279px;height:88px;background:linear-gradient(180deg,#ffffff,#e9e9e9);
  border:1px solid #d4d4d4;box-shadow:0 1px 3px rgba(0,0,0,.25)}
.brand .mark{position:absolute;right:18px;top:13px;width:28px;height:28px;background:var(--blue)}
.brand .name{position:absolute;left:16px;top:55px;font-family:"Open Sans",sans-serif;font-weight:600;font-size:19px;color:#555}
.hero-box{position:absolute;left:111px;top:470px;width:713px;height:152px;background:rgba(46,111,176,.93);padding:18px 28px}
.hero-box h1{font-family:"Carlito",sans-serif;font-weight:700;font-size:50px;line-height:1;letter-spacing:-1.4px;color:var(--white)}
.hero-box p{margin-top:16px;font-family:"Carlito",sans-serif;font-size:16.5px;line-height:21px;letter-spacing:-.3px;color:#eaf2fb}
.features{position:absolute;left:0;top:754px;width:1093px;height:184px;background:var(--band)}
.feature{position:absolute;top:30px;width:230px}
.feature h2{font-family:"Sintony",sans-serif;font-weight:400;font-size:17px;color:#444;display:flex;align-items:center;gap:12px;height:28px}
.feature p{margin-top:10px;font-family:"Open Sans",sans-serif;font-size:13px;line-height:18px;color:var(--muted)}
.feature a,.feature cite{display:block;margin-top:14px;font-family:"Sintony",sans-serif;font-size:11.5px;color:var(--link);text-decoration:none}
.feature cite{font-style:italic}
.chevron{position:absolute;top:0;height:184px;width:40px}
.welcome{position:absolute;left:0;top:938px;width:1093px;height:214px;background:var(--dark)}
.welcome h2{position:absolute;left:119px;top:30px;font-family:"Sintony",sans-serif;font-weight:400;font-size:27px;color:var(--white)}
.welcome .intro{position:absolute;left:119px;top:86px;width:522px;font-size:12.5px;line-height:17.8px;color:var(--dark-text);letter-spacing:.2px}
.rule{position:absolute;border-top:1px dotted #6d6d6d}
.signup h3{position:absolute;left:716px;top:35px;font-family:"Sintony",sans-serif;font-weight:400;font-size:19px;color:var(--white)}
.signup p{position:absolute;left:716px;top:86px;font-size:12.5px;color:var(--dark-text)}
.signup .email{position:absolute;left:715px;top:112px;width:257px;height:32px;background:#fafafa;border:1px solid #ccc;
  font-size:13px;color:#aaa;padding:7px 12px}
.signup .subscribe{position:absolute;left:715px;top:156px;width:79px;height:26px;border-radius:3px;
  background:linear-gradient(180deg,#2aa3f0,#1484d6);color:var(--white);font-family:"Sintony",sans-serif;font-weight:700;font-size:11px;
  text-align:center;line-height:26px}
.footer{position:absolute;left:0;top:1152px;width:1093px;height:48px;background:var(--footer);border-top:4px solid var(--blue)}
.footer .copy{position:absolute;left:119px;top:17px;font-size:11.5px;color:#444}
.footer nav a{position:absolute;top:17px;font-size:11.5px;color:#444;text-decoration:none}
.footer .pointer{position:absolute;left:657px;top:0}
</style>
</head>
<body>

<div class="hero-photo" role="img" aria-label="Black and white aerial photograph of London at dusk with the winding Thames and Tower Bridge lit up"></div>

<header class="topbar">
  <span class="call">Call Us&nbsp; 1-800&nbsp; 555 0142</span>
  <span class="social" style="left:899px;background:#4fb3e8"></span>
  <span class="social" style="left:926px;background:#3b64b0"></span>
  <span class="social" style="left:952px;background:#f08a1c"></span>
</header>

<div class="nav-band">
  <nav class="nav">
    <a href="#" style="left:441px">Home</a>
    <a href="#" style="left:533px">About Us</a>
    <a href="#" style="left:648px">Managed Account</a>
    <a href="#" style="left:816px">System Performance</a>
  </nav>
</div>

<div class="brand">
  <span class="mark"></span>
  <span class="name">brightwell capital</span>
</div>

<section class="hero-box">
  <h1>Integrity, Innovative, Progressive</h1>
  <p>Le Lorem Ipsum est simplement du faux textet employé dans la composition et la mise en page avant impression.&nbsp; l'imprimerie depuis les années 1500</p>
</section>

<section class="features">
  <svg class="chevron" style="left:368px" viewBox="0 0 40 184"><path d="M0 0 L40 92 L0 184 Z" fill="#ececec"/></svg>
  <svg class="chevron" style="left:666px" viewBox="0 0 40 184"><path d="M0 0 L40 92 L0 184 Z" fill="#ececec"/></svg>
  <svg class="chevron" style="left:955px" viewBox="0 0 40 184"><path d="M0 0 L40 92 L0 184 Z" fill="#ececec"/></svg>

  <article class="feature" style="left:118px">
    <h2>Fund Management
      <svg width="26" height="28" viewBox="0 0 26 28"><path d="M13 1 L25 5 V13 C25 20 19 25 13 27 C7 25 1 20 1 13 V5 Z" fill="#555"/><circle cx="13" cy="13" r="4" fill="#fff"/></svg>
    </h2>
    <p>Lorem Ipsum est simplement du faux texte employé dans la composition et la mise en page avant impression.</p>
    <a href="#" style="margin-top:20px">Read more</a>
  </article>

  <article class="feature" style="left:429px">
    <h2>Algorithmic Design
      <svg width="26" height="26" viewBox="0 0 26 26"><circle cx="13" cy="13" r="12.5" fill="#555"/><path d="M8.5 9 A6.5 6.5 0 1 0 17.5 9" fill="none" stroke="#fff" stroke-width="2"/><path d="M13 6 V13" stroke="#fff" stroke-width="2"/></svg>
    </h2>
    <p>Lorem Ipsum est simplement du faux texte employé dans la composition et la mise en page avant impression.</p>
    <a href="#">Read more</a>
  </article>

  <article class="feature" style="left:723px">
    <h2>Testimonials
      <svg width="26" height="26" viewBox="0 0 26 26"><path d="M2 2 L24 24" stroke="#555" stroke-width="4" stroke-linecap="round"/></svg>
    </h2>
    <p>“Lorem Ipsum est simplement du faux texte employé dans la composition et la mise en page avant impression.”</p>
    <cite>Marcus Ellery</cite>
  </article>
</section>

<section class="welcome">
  <h2>Welcome to Brightwell Capital</h2>
  <span class="rule" style="left:119px;top:73px;width:522px"></span>
  <p class="intro">Lorem ipsum dolor sit amet, consectetuer adipiscing elit, sed diam nonummy nibh euismod tincidunt ut laoreet dolore magna aliquam erat volutpat. Ut wisi enim ad minim veniam, quis nostrud exerci tation ullamcorper suscipit lobortis nisl ut aliquip ex ea commodo consequat.uis autem vel eum iriure dolor in hendrerit in vulputate velit esse molestie consequat.</p>

  <div class="signup">
    <h3>NewsLetter Signup</h3>
    <span class="rule" style="left:716px;top:73px;width:280px"></span>
    <p>Lorem ipsum dolor sit amet, consectet</p>
    <div class="email">Enter Email</div>
    <div class="subscribe">Subscribe</div>
  </div>
</section>

<footer class="footer">
  <svg class="pointer" width="16" height="10" viewBox="0 0 16 10"><path d="M0 0 H16 L8 10 Z" fill="var(--blue)"/></svg>
  <span class="copy">© Brightwell Capital, All rights reserved.</span>
  <nav>
    <a href="#" style="left:615px">Home</a>
    <a href="#" style="left:665px">About Us</a>
    <a href="#" style="left:732px">Services</a>
    <a href="#" style="left:796px">News &amp; Comments</a>
    <a href="#" style="left:915px">Contact Us</a>
  </nav>
</footer>

</body>
</html>
```